Hurricane Damage Public Adjuster Billboard

I have created several projects with you and have several great designs. I need to format them into a Billboard for upcoming Hurricane Season. Need done in a month. Im also in process of getting an eye catching and easy to remember 800# Vanity phone number like Call 800-Stormfix or 800- Need Help? My included past Sketch Guild projects will give you an idea of what colors, schemes, and designs I gravitate towards. 3 past Design projects were 1) 2 Logos where I picked the 1st place and the 2nd place and 2) Index Card where I picked the winner as the Index Card and the 2nd place as a Post Card. Point is, I will pick and pay for 2 winners if they're good. This should help to sweeten the pot. Also, please look at my website for ideas that I like:

www.TheClaimWardenGroup.com
I want people to feel that I am the best and highest. Level.

I've been getting a lot of quick half effort designs basically cut & pasting my previous projects. Please don't rush and take your time to be creative. A an example, my Biggest Competitor is Crestline Public Adjusting. Their colors are Black and Gold while mine are Blue, White, and Black with a highlight of Orange if possible. I JUST imported a picture of their BillBoard. I need mine better and BLOW AWAY THEIRS. Terms like "Don't be Victimized Twice ?, Don't let the Hurricane Ruin your Life?". "Get Fairly Paid & Move On" "Our Clients Claims are VIP?
Updates

I'm getting a lot of quick half effort ones. I'd rather you take your time and really put some thoughts and effort into it. My Biggest Competitor is Crestline Public Adjusting. They have black & gold colors, while I have Blue, Black, and white.

It needs to blow theirs away. I have imported their Billboard for comparative purposes.

Guy's,
I'll make it easier for you in what I'm looking for. Please look at the Crestline Billboard picture attached.

1) Put my "Blue Shield" to the left, replacing their logo
2) change color patterns from their (Black, Gold, White) to my color schemes of (Black, Blue, White)
3) I want to see my name where their is:

THE
Claim Warden Group
EXPERT & LOCAL Public Adjusters
"FOR THE POLICYHOLDER!!"

4) to the right, add the A+Rated logo and QTR+ Accredited logo, 5 Star Zentrio Rated logo, 5 Start BLOCKLINK Highly Rated logo, etc..

5) the right side is where you can be creative as I will not have a picture of me there.

"20+ Years of Experience, Recovering Millions for our VIP Clients"

"Your Best, Locally-Based Private Adjuster & Advocate'
"FOR THE POLICYHOLDER!!"

"Don't be victimized Twice!!"

"Don't let the Hurricane Ruin Your Life!!"

This should really help. Also, refer to my website, maybe a couple testimonial fillers?

Thanks all,

marvin@TheClaimWardenGroup.com

Just imported a few awards that would look great to the right side with all the other 5 Star Ratings and accolades.
This right section could be titled like zmy Website:

5 Star Reviews, Ratings & Awards:
4-5 Logos underneath?

Target Market(s)

Coastal place where a Hurricane 🌀 🌀 Hits

Industry/Entity Type

Hurricane Public Insurance Adjuster

Font styles to use
Sans Serif
Other font styles liked:
• Calvera fonts

Colors
0054AA
0677BA
7BADD7
CADEEF
E8F1F8
EE7325
F08F49
F5BC92
FAE3D3
FDF4ED

Requirements
Must have
• Use my past project logos, colors, and schemes to create eye grabbing BillBoard
Nice to have
Should not have
• Not be too busy, must be Easy to Read, Eye Catchy

```html
<!DOCTYPE html>
<html lang="en">
<head>
<meta charset="utf-8">
<title>Claim Warden Group Billboard</title>
<link href="https://fonts.googleapis.com/css2?family=Playfair+Display:wght@400&family=Oswald:wght@400;600&family=Montserrat:wght@500;700&family=Allura&family=Noto+Serif:wght@400&family=Archivo+Black&display=swap" rel="stylesheet">
<style>
  :root{
    --ink:#000000;
    --paper:#ffffff;
    --brand-blue:#0a8fd8;
    --brand-cyan:#12b8ee;
    --deep-blue:#0054aa;
    --alert-red:#e8262b;
    --storm-dark:#1d2336;
    --storm-purple:#6d5a86;
    --storm-light:#b9a9cf;
  }
  *{box-sizing:border-box;margin:0;padding:0}
  html,body{width:1189px;height:1200px;overflow:hidden;background:var(--paper)}
  .billboard{position:absolute;left:44px;top:439px;width:1100px;height:322px;background:var(--ink);overflow:hidden}
  .brand-mark{position:absolute;left:40px;top:70px;width:230px;text-align:center}
  .brand-mark .square{width:56px;height:56px;background:var(--brand-blue);margin:0 auto 16px}
  .brand-mark .name{font-family:"Montserrat",sans-serif;font-weight:700;font-size:26px;line-height:1.15;color:var(--brand-blue)}
  .headline{position:absolute;left:300px;top:18px;width:390px;text-align:center;color:var(--paper);font-family:"Playfair Display",serif;font-weight:400;line-height:.95}
  .headline .line{display:block;font-size:43px;letter-spacing:-.5px}
  .headline .line.big{font-size:56px;margin-top:4px}
  .headline .script{font-family:"Allura",cursive;color:var(--brand-blue);font-size:72px;margin-left:-4px}
  .credential{position:absolute;left:300px;top:186px;width:368px;height:60px;border:2px solid var(--paper);display:flex;align-items:center;padding:0 8px;color:var(--paper)}
  .credential .tag{font-family:"Montserrat",sans-serif;font-weight:500;font-size:9.5px;line-height:1.2;width:186px}
  .credential .tag strong{font-weight:700}
  .credential .arrow{width:24px;height:22px;margin:0 8px}
  .credential .person{font-family:"Archivo Black","Montserrat",sans-serif;font-size:21px;line-height:1;text-align:center;flex:1;letter-spacing:.5px}
  .call-strip{position:absolute;left:14px;top:266px;width:334px;height:43px;background:var(--paper);clip-path:polygon(0 0,100% 0,97% 100%,0 100%);font-family:"Oswald",sans-serif;font-size:33px;line-height:43px;color:var(--ink);padding-left:16px;letter-spacing:-.5px}
  .call-strip b{font-weight:600}
  .web-strip{position:absolute;left:340px;top:266px;width:362px;height:43px;background:var(--brand-blue);clip-path:polygon(3% 0,100% 0,97% 100%,0 100%);font-family:"Oswald",sans-serif;font-size:27px;line-height:43px;color:var(--paper);padding-left:22px;letter-spacing:-.3px}
  .web-strip b{font-weight:600}
  .scene{position:absolute;left:700px;top:0;width:400px;height:252px;clip-path:polygon(12% 0,100% 0,100% 100%,0 100%);background:
    radial-gradient(ellipse at 55% 25%,var(--storm-light) 0%,transparent 35%),
    radial-gradient(ellipse at 50% 75%,#6a4a2a 0%,transparent 30%),
    linear-gradient(180deg,var(--storm-purple) 0%,var(--storm-dark) 55%,#1a2a1e 100%)}
  .rating{position:absolute;left:722px;top:256px;width:165px;text-align:center}
  .rating .grade{font-family:"Archivo Black","Montserrat",sans-serif;font-size:28px;line-height:1;color:var(--alert-red)}
  .rating .note{font-family:"Noto Serif",serif;font-size:10px;line-height:1.1;color:var(--paper)}
  .badges{position:absolute;left:892px;top:262px;display:flex;gap:4px}
  .badge{height:40px;background:var(--paper)}
  .badge.wide{width:84px;background:var(--deep-blue);border:3px solid var(--paper)}
  .badge.seal{width:44px;background:#d9b64a}
  .badge.award{width:32px;background:#3a4d7a}
</style>
</head>
<body>
  <div class="billboard">
    <div class="brand-mark">
      <div class="square"></div>
      <div class="name">Claim Warden Group</div>
    </div>

    <h1 class="headline">
      <span class="line">DON'T LET THE</span>
      <span class="line">HURRICANE RUIN</span>
      <span class="line big">YOUR<span class="script">Life!!</span></span>
    </h1>

    <div class="credential">
      <p class="tag">THE<br>Claim Warden Group<br>EXPERT &amp; LOCAL Public Adjusters<br><strong>"FOR THE POLICYHOLDER!!"</strong></p>
      <svg class="arrow" viewBox="0 0 24 22" aria-hidden="true"><path d="M0 0 L12 11 L0 22 Z M10 0 L22 11 L10 22 Z" fill="#0a8fd8"/></svg>
      <p class="person">MARVIN<br>KESSLER</p>
    </div>

    <div class="call-strip">CALL <b>800-STORMFIX</b></div>
    <div class="web-strip">The<b>ClaimWardenGroup</b>.com</div>

    <div class="scene" role="img" aria-label="Photo of a lit house at night under a lightning storm"></div>

    <div class="rating">
      <p class="grade">A+ Rating</p>
      <p class="note">High Rating For<br>Public Insurance Adjusters</p>
    </div>

    <div class="badges">
      <div class="badge wide"></div>
      <div class="badge seal"></div>
      <div class="badge award"></div>
    </div>
  </div>
</body>
</html>
```